Business Card Design for Consulting Company

I require a Business Card design for my Consulting company. <br/><br/>My company name is: Marek Olvani Consulting Inc.<br/>My website is: www.marekolvaniconsulting.example<br/><br/>My company focuses on management and software development for the Tallobrix CRM platform (www.tallobrix.example)<br/><br/>I have a logo already designed...see attached.
Updates

Also Include my Name and Title: Marek T.L. Olvani President

Target Market(s)

Tallobrix Customers

Contact Information for Business Card

Only include my LOGO (provided)
My Name: Marek TL Olvani
My Title: President
My Company Name: Marek Olvani Consulting Inc.
My Website: www.marekolvaniconsulting.example
My Email: marek.olvani.consulting@mailbox.example

NO PHONE NUMBER
NO ADDRESS

Font styles to use
Serif
Sans Serif
Other font styles liked:
• see my website: www.marekolvaniconsulting.example

Colors

Designer to choose colors to be used in the design.

Requirements
Must have
• Must include my Orange
• Include my name (Marek T.L. Olvani), title (President) company name, website and email
• It should also have a tag line like: Tallobrix Consulting
• I'm flexible with the tag line
Should not have
• Don't include my phone number or address

```html
<!DOCTYPE html>
<html lang="en">
<head>
<meta charset="utf-8">
<title>Marek Olvani Consulting Inc. – Business Card</title>
<link rel="stylesheet" href="https://fonts.googleapis.com/css2?family=Exo+2:wght@300;600&family=Open+Sans:wght@400&display=swap">
<style>
  :root {
    --backdrop: #3a3d42;
    --card-blue: #1f5782;
    --card-blue-dark: #194a70;
    --brand-orange: #ff8a0a;
    --paper-white: #ffffff;
    --soft-white: #dbe6f0;
    --ink: #222a33;
    --display-font: "Exo 2", sans-serif;
    --body-font: "Open Sans", sans-serif;
  }
  * { margin: 0; padding: 0; box-sizing: border-box; }
  html, body {
    width: 789px; height: 1200px; overflow: hidden;
    background: var(--backdrop);
  }
  .canvas {
    position: relative; width: 789px; height: 1200px;
    background: radial-gradient(ellipse at 50% 40%, #4a4e54 0%, var(--backdrop) 70%);
  }
  .card {
    position: absolute; left: 74px; width: 640px; height: 366px;
    overflow: hidden;
    box-shadow: 0 14px 30px rgba(0,0,0,.45);
  }
  /* Front side */
  .card-front {
    top: 150px;
    background: linear-gradient(160deg, #23618f 0%, var(--card-blue) 45%, var(--card-blue-dark) 100%);
    border-left: 14px solid var(--brand-orange);
    border-right: 14px solid var(--brand-orange);
  }
  .front-mark {
    position: absolute; left: 0; right: 0; top: 110px;
    text-align: center;
    font-family: var(--display-font); font-weight: 600;
    font-size: 54px; letter-spacing: 1px; line-height: 1;
    color: var(--brand-orange);
  }
  .front-company {
    position: absolute; left: 0; right: 0; top: 192px;
    text-align: center;
    font-family: var(--display-font); font-weight: 300;
    font-size: 24px; letter-spacing: .5px; line-height: 1.2;
    color: var(--paper-white);
  }
  .front-tagline {
    position: absolute; left: 0; right: 0; top: 236px;
    text-align: center;
    font-family: var(--display-font); font-weight: 300;
    font-size: 15px; letter-spacing: 3px; text-transform: uppercase;
    color: var(--brand-orange);
  }
  /* Back side */
  .card-back { top: 660px; background: var(--paper-white); }
  .card-back svg.wave { position: absolute; inset: 0; }
  .back-heading {
    position: absolute; left: 40px; top: 50px;
    display: flex; align-items: center; gap: 16px;
  }
  .brand-square {
    width: 34px; height: 34px; background: var(--brand-orange);
  }
  .back-company {
    font-family: var(--display-font); font-weight: 300;
    font-size: 27px; letter-spacing: .5px; line-height: 1;
    color: var(--paper-white);
  }
  .holder {
    position: absolute; left: 90px; top: 100px;
    font-family: var(--display-font); font-weight: 300;
    font-size: 17px; letter-spacing: .5px;
    color: var(--soft-white);
  }
  .holder-title { color: var(--brand-orange); margin-left: 10px; }
  .contact-list {
    position: absolute; right: 24px; top: 244px;
    list-style: none;
    font-family: var(--body-font); font-size: 14px; color: var(--ink);
  }
  .contact-list li {
    display: flex; justify-content: flex-end; align-items: center;
    gap: 12px; height: 30px;
  }
  .contact-icon { width: 24px; height: 24px; flex: none; }
  .footer-rule {
    position: absolute; left: 260px; right: 30px; top: 336px;
    height: 1px; background: var(--brand-orange);
  }
</style>
</head>
<body>
<main class="canvas">

  <section class="card card-front" aria-label="Card front">
    <div class="front-mark">Marek Olvani</div>
    <div class="front-company">Marek Olvani Consulting Inc.</div>
    <div class="front-tagline">Tallobrix Consulting</div>
  </section>

  <section class="card card-back" aria-label="Card back">
    <svg class="wave" viewBox="0 0 640 366" width="640" height="366" aria-hidden="true">
      <defs>
        <linearGradient id="whiteFade" x1="0" y1="0" x2="0" y2="1">
          <stop offset="0" stop-color="#f0f2f4"/>
          <stop offset="1" stop-color="#ffffff"/>
        </linearGradient>
      </defs>
      <rect width="640" height="366" fill="url(#whiteFade)"/>
      <path d="M0,0 H640 V92 C500,100 420,160 320,240 C240,300 140,335 0,335 Z" fill="#1f5782"/>
      <path d="M640,92 C500,100 420,160 320,240 C240,300 140,335 0,335" fill="none" stroke="#ff8a0a" stroke-width="4"/>
      <path d="M640,104 C506,112 428,172 330,252 C252,312 150,346 0,347" fill="none" stroke="#ff8a0a" stroke-width="1"/>
    </svg>

    <div class="back-heading">
      <span class="brand-square"></span>
      <span class="back-company">Marek Olvani Consulting Inc.</span>
    </div>
    <p class="holder">Marek T.L. Olvani<span class="holder-title">President</span></p>

    <ul class="contact-list">
      <li>marek.olvani.consulting@mailbox.example
        <svg class="contact-icon" viewBox="0 0 24 24" aria-hidden="true">
          <circle cx="12" cy="12" r="12" fill="#1f5782"/>
          <rect x="6.5" y="8" width="11" height="8" fill="none" stroke="#fff" stroke-width="1.2"/>
          <path d="M6.5,8 L12,12.5 L17.5,8" fill="none" stroke="#fff" stroke-width="1.2"/>
        </svg>
      </li>
      <li>www.marekolvaniconsulting.example
        <svg class="contact-icon" viewBox="0 0 24 24" aria-hidden="true">
          <circle cx="12" cy="12" r="12" fill="#1f5782"/>
          <circle cx="12" cy="12" r="6" fill="none" stroke="#fff" stroke-width="1.2"/>
          <ellipse cx="12" cy="12" rx="2.6" ry="6" fill="none" stroke="#fff" stroke-width="1"/>
          <path d="M6,12 H18" stroke="#fff" stroke-width="1"/>
        </svg>
      </li>
    </ul>

    <div class="footer-rule"></div>
  </section>

</main>
</body>
</html>
```